Cradle Quill

This is a single-page full-screen tablet app that generates baby names based on a few user-selected options. The code is already written; I just need the visual design.
UI elements are:
1) Options, containing:
i) Gender selector
ii) Multi-select
inspiration sources (names based on country of origin)
iii) Scroll speed selector
2) Favourites panel containing list of current favourites (with UI to delete items)
3) Output panel; a live scrolling list of generated names - click to add as a favourite.
The app is a Panelix 8 Tessel application, written in XAML. It should stick to the Tessel conventions/spirit. Here are some docs/samples:
http://docs.brightvane.example/library/panes/apps/qx482015/
http://en.lorepedia.example/wiki/Tessel_(design_language)
Ideally, design will be presented in XAML format.
The attached design is the crap I've got meanwhile - it shows the basic elements. The list of generated names appears in the white-space on the right. The bar on the bottom is an advertisement.
More on the Tessel design principles that should be adhered to:
http://www.brightvane.example/design/toolbox/tutorials/pane-handset-7/tessel/
Ideal submission would be in XAML format. However, Adobe Illustrator files are decent as well; vector format is important.
Pixel-based images aren't ideal in this case, because Tessel applications need to be scalable to any resolution.
Target Market(s)
People expecting a baby; mostly women.
Industry/Entity Type
Baby
Look and feel

```html
<!DOCTYPE html>
<html lang="en">
<head>
<meta charset="utf-8">
<title>Cradle Quill</title>
<link href="https://fonts.googleapis.com/css2?family=Dosis:wght@500;600;700&family=Carlito&display=swap" rel="stylesheet">
<style>
  :root {
    --ink-navy: #1f2a6b;
    --boy-blue: #2f8fd6;
    --girl-pink: #f27fae;
    --track-blue: #3f86de;
    --panel-bg: #ffffff;
    --rule: #d9dce2;
    --name-ink: #1e1e1e;
    --header-top: #a9b6cb;
    --header-bottom: #6d7f9c;
    --grey-top: #9b9b9b;
    --grey-bottom: #5d5d5d;
    --index-ink: #8a8f99;
  }
  * { box-sizing: border-box; margin: 0; padding: 0; }
  html, body { width: 1200px; height: 616px; overflow: hidden; background: #fff; }
  .app { position: relative; width: 1200px; height: 616px; font-family: "Carlito", "Calibri", sans-serif; }

  .display { font-family: "Dosis", "Arial Narrow", sans-serif; font-weight: 700; text-transform: uppercase; }

  /* speed slider */
  .speed { position: absolute; left: 48px; top: 55px; display: flex; align-items: center; gap: 8px; color: var(--ink-navy); font-size: 17px; }
  .speed-track { position: relative; width: 156px; height: 11px; border-radius: 6px; border: 1px solid #b8bcc6; background: #f2f3f6; }
  .speed-fill { position: absolute; left: 0; top: 0; bottom: 0; width: 78px; border-radius: 6px 0 0 6px; background: linear-gradient(#7fb2ee, var(--track-blue)); }
  .speed-thumb { position: absolute; left: 64px; top: -11px; width: 31px; height: 31px; border-radius: 50%; background: radial-gradient(circle at 45% 35%, #fff, #d6d8dc 70%, #b7bac0); border: 1px solid #a8abb2; box-shadow: 0 1px 3px rgba(0,0,0,.25); }

  /* gender */
  .gender { position: absolute; top: 138px; display: flex; flex-direction: column; align-items: center; gap: 12px; font-size: 17px; }
  .gender-dot { width: 46px; height: 46px; border-radius: 50%; box-shadow: 0 3px 5px rgba(0,0,0,.25); }
  .gender.boy { left: 53px; color: var(--boy-blue); }
  .gender.boy .gender-dot { background: radial-gradient(circle at 40% 35%, #e4f6ff, #9fd9f4 70%, #7cc6ec); }
  .gender.girl { left: 114px; color: var(--girl-pink); }
  .gender.girl .gender-dot { background: radial-gradient(circle at 40% 35%, #ffe6ef, #f9a7c6 70%, #f288b1); }

  /* panels */
  .panel { position: absolute; background: var(--panel-bg); box-shadow: 0 1px 7px rgba(0,0,0,.3); }
  .bar-grey { background: linear-gradient(var(--grey-top), var(--grey-bottom)); color: #fff; }
  .bar-blue { background: linear-gradient(var(--header-top), var(--header-bottom)); color: #fff; border-top: 1px solid #55627a; border-bottom: 1px solid #55627a; }

  .inspiration { left: 40px; top: 305px; width: 339px; height: 237px; }
  .inspiration-title { height: 38px; display: flex; align-items: center; justify-content: center; font-size: 17px; font-weight: 600; letter-spacing: .5px; }
  .flag { position: absolute; width: 89px; height: 62px; border: 1px solid #fff; box-shadow: 0 2px 4px rgba(0,0,0,.55); }
  .flag-label { position: absolute; left: 50px; top: 128px; width: 100px; text-align: center; font-family: "Dosis", sans-serif; font-weight: 500; font-size: 13px; color: #555; }

  .names { left: 446px; top: 57px; width: 345px; height: 485px; }
  .names-title { position: absolute; left: 15px; top: 16px; width: 316px; height: 47px; display: flex; align-items: center; justify-content: center; font-size: 21px; letter-spacing: .5px; }
  .letter-bar { position: absolute; left: 15px; top: 63px; width: 316px; height: 20px; background: linear-gradient(#9a9a9a, #c9c9c9); color: #fff; font-size: 15px; padding-left: 8px; line-height: 20px; opacity: .9; z-index: 2; }
  .name-list { position: absolute; left: 15px; top: 69px; width: 287px; list-style: none; }
  .name-list li { height: 44px; border-bottom: 1px solid var(--rule); font-size: 19px; color: var(--name-ink); padding-left: 10px; line-height: 52px; }
  .name-list li:first-child { height: 24px; line-height: 20px; }
  .alpha-index { position: absolute; left: 309px; top: 68px; width: 14px; list-style: none; text-align: center; font-size: 10px; line-height: 13.7px; color: var(--index-ink); font-family: "Dosis", sans-serif; }

  .favourites { left: 823px; top: 57px; width: 343px; height: 485px; }
  .favourites-title { position: absolute; left: 12px; top: 9px; width: 319px; height: 43px; display: flex; align-items: center; justify-content: center; font-size: 20px; letter-spacing: .5px; }
  .fade-bar { position: absolute; left: 12px; top: 52px; width: 319px; height: 22px; background: linear-gradient(#9c9c9c, #d0d0d0); opacity: .85; z-index: 2; }
  .fav-list { position: absolute; left: 12px; top: 53px; width: 319px; list-style: none; }
  .fav-list li { height: 44px; border-bottom: 1px solid var(--rule); font-size: 19px; color: var(--name-ink); padding-left: 10px; line-height: 52px; }
  .fav-list li:first-child { height: 45px; line-height: 24px; }
</style>
</head>
<body>
<main class="app">
  <div class="speed display">
    <span>Slower</span>
    <div class="speed-track"><div class="speed-fill"></div><div class="speed-thumb"></div></div>
    <span>Faster</span>
  </div>

  <div class="gender boy display"><div class="gender-dot"></div><span>Boy</span></div>
  <div class="gender girl display"><div class="gender-dot"></div><span>Girl</span></div>

  <section class="panel inspiration">
    <h2 class="inspiration-title bar-grey display">Inspiration</h2>
    <div class="flag" role="img" aria-label="Russian flag" style="left:11px;top:49px;background:linear-gradient(#f4f4f4 33%,#2f4fb8 33% 66%,#d2242b 66%)"></div>
    <div class="flag" role="img" aria-label="United States flag" style="left:106px;top:49px;background:linear-gradient(135deg,#2d3e86 35%,#c7343f 35%,#e8e2e2 70%,#c7343f)"></div>
    <div class="flag" role="img" aria-label="Chinese flag" style="left:219px;top:49px;background:linear-gradient(#d33a33,#b8231f)"></div>
    <span class="flag-label">US Names</span>
    <div class="flag" role="img" aria-label="Irish flag" style="left:11px;top:153px;background:linear-gradient(90deg,#2f7a3d 33%,#f1f1f1 33% 66%,#e07a2a 66%)"></div>
    <div class="flag" role="img" aria-label="Italian flag" style="left:106px;top:153px;background:linear-gradient(90deg,#2f8a46 33%,#f1f1f1 33% 66%,#cf2e36 66%)"></div>
    <div class="flag" role="img" aria-label="Indian flag" style="left:219px;top:153px;background:linear-gradient(#ea9a52 33%,#f4f4f4 33% 66%,#2f8a3c 66%)"></div>
  </section>

  <section class="panel names">
    <h2 class="names-title bar-blue display">Names</h2>
    <div class="letter-bar">A</div>
    <ul class="name-list">
      <li>Ada</li><li>Anastasia</li><li>Anna</li><li>Annamaria</li><li>Adriana</li><li>Amalia</li><li>Almata</li><li>Andromeda</li>
    </ul>
    <ul class="alpha-index">
      <li>A</li><li>B</li><li>C</li><li>D</li><li>E</li><li>F</li><li>G</li><li>H</li><li>I</li><li>J</li><li>K</li><li>L</li><li>M</li><li>N</li><li>O</li><li>P</li><li>Q</li><li>R</li><li>S</li><li>T</li><li>U</li><li>V</li><li>W</li><li>X</li><li>Y</li><li>Z</li><li>#</li>
    </ul>
  </section>

  <section class="panel favourites">
    <h2 class="favourites-title bar-blue display">Favourites</h2>
    <div class="fade-bar"></div>
    <ul class="fav-list">
      <li>Ada</li><li>Laura</li><li>Roberta</li><li>Giulia</li><li>Adriana</li><li>Sara</li><li></li><li></li>
    </ul>
  </section>
</main>
</body>
</html>
```